Freelance film producer/editor wants you to gleam nova!

'Gleam Nova' is my production business based in Melbourne, though I do a fair bit of work overseas. I'm a one woman show most of the time but enlist other crew members for larger projects. I manage productions from start to finish including producing, filming, editing, distribution, photography and animation.

My current tag line and details are as follows:

Petra Vandoren
Producer. Editor. Thinker.
[M] +61 492 157 630
[E] pv[at]brightpanel.com.au
www.brightpanel.com.au

I have a fairly wicked sense of humour and love a good pun, so feel free to work this into your design!

The final designs should demonstrate the areas I work in but not limited to. I'd rather not use old and typical "film" looking elements such as a clapper or negative reel. Having said that, the logo itself (attached) is quite typical because the first 'o' is a closed aperture and the second is a wide aperture. Happy for the logo to be pulled apart for the business card to be more interesting.

The majority of projects I work on are quite different and in some cases a bit crazy. Lots of travel involved. The main difference between me and other producers is that I don't say I work in 'film', even though i do. I want the card to leave me open to new roles and projects as opposed to squashing myself into one particular category.

I'm open to colour but prefer a simple design that isn't too hectic.

I have also attached an example I did like that was printed on plastic but then I realised so many other people had ripped it off....

I'm open to paper board or plastic (transparent) designs etc. One sided or two sided.

Thanks for sharing your ideas with me and please, go as nuts as you want to with this! :)

Target Market(s)

My clients range from non profits in health and educational institutions to record labels and well known artists. The business attracts corporates as well though the majority of my business is achieved through referral and word of mouth so most people will soon realise that my personality and work are very much intertwined and the reason they hire me for a job.

Industry/Entity Type

Business

Font styles to use
Other font styles liked:
• Eurostile or similar

Requirements
Must have
• I have a very open mind when it comes to design. I do like the existing tag line but if you can come up with something better I'm all ears! (and eyes)

Nice to have
• Back of the business card can be graphics, there can be transparent elements or holes, embossing options...
Should not have
• Besides my name, nothing should scream "I am woman!" because in my industry that's not a selling point.

The colour pink is a definite no.

```html
<!DOCTYPE html>
<html lang="en">
<head>
<meta charset="utf-8">
<title>Petra Vandoren — Business Card</title>
<link rel="stylesheet" href="https://fonts.googleapis.com/css2?family=Saira+Semi+Condensed:wght@400&family=Saira:wght@400&family=Questrial&display=swap">
<style>
  :root {
    --sky: #5fd0f0;
    --sky-deep: #39b6e4;
    --sea: #2fc1b4;
    --sea-deep: #1a9fa0;
    --lens-edge: #0d2f6b;
    --veil: rgba(255, 255, 255, 0.28);
    --veil-strong: rgba(255, 255, 255, 0.55);
    --name: #1f8aa0;
    --tagline: #5ec9ef;
    --web: #121212;
  }
  * { margin: 0; padding: 0; box-sizing: border-box; }
  html, body {
    width: 1200px;
    height: 700px;
    overflow: hidden;
    background: #ffffff;
  }
  .card {
    position: relative;
    width: 1200px;
    height: 700px;
    overflow: hidden;
  }
  .card__scene {
    position: absolute;
    inset: 0;
    background:
      radial-gradient(ellipse 62% 92% at 50% 50%, rgba(13,47,107,0) 88%, var(--lens-edge) 100%),
      linear-gradient(180deg, var(--sky) 0%, var(--sky-deep) 28%, #a8ecf4 50%, var(--sea) 68%, var(--sea-deep) 100%);
  }
  .card__veil {
    position: absolute;
    left: 127px;
    top: 116px;
    width: 930px;
    height: 453px;
    background: var(--veil);
  }
  .card__panel {
    position: absolute;
    left: 162px;
    top: 141px;
    width: 867px;
    height: 392px;
    background: linear-gradient(180deg, var(--veil-strong) 0%, rgba(255,255,255,0.72) 45%, rgba(255,255,255,0.35) 100%);
  }
  .card__name {
    position: absolute;
    left: 0;
    width: 1198px;
    top: 172px;
    text-align: center;
    white-space: nowrap;
    font-family: "Saira Semi Condensed", "Eurostile", sans-serif;
    font-weight: 400;
    font-size: 124px;
    line-height: 1;
    color: var(--name);
  }
  .card__tagline {
    position: absolute;
    left: 0;
    width: 1164px;
    top: 302px;
    text-align: center;
    white-space: nowrap;
    font-family: "Saira", "Eurostile", sans-serif;
    font-weight: 400;
    font-size: 57px;
    line-height: 1;
    color: var(--tagline);
    letter-spacing: 1px;
  }
  .card__web {
    position: absolute;
    left: 0;
    width: 1144px;
    top: 388px;
    text-align: center;
    white-space: nowrap;
    font-family: "Questrial", sans-serif;
    font-size: 52px;
    line-height: 1;
    color: var(--web);
    letter-spacing: 0.5px;
  }
</style>
</head>
<body>
  <main class="card">
    <div class="card__scene" role="img" aria-label="Fisheye photograph of a beach with blue sky, turquoise sea and swimmers near the shore"></div>
    <div class="card__veil"></div>
    <div class="card__panel"></div>
    <h1 class="card__name">Petra Vandoren</h1>
    <p class="card__tagline">Producer. Editor. Thinker.</p>
    <p class="card__web">www.brightpanel.com.au</p>
  </main>
</body>
</html>
```